sticker for cleaning products

it is in the bottle. products are bio-cleaner. Toilet Cleaner - yellow Sanitary Cleaner - orange Glass Cleaner - light blue All purpose cleaner - green Hand Soap - cream Detergent - olive Detergent - rose bottles is used VARIO: https://glasbehaelterwelt.de/angebot/#Serie shape of the sticker is not geometric. It's something like a cloud / leaf / drop / ?? the sticker has an inner space with only the product name and color. the sticker has an outer space. here we want to mark out "powered by BRENOSKI" (our company name, find logo attached)

```html
<!DOCTYPE html>
<html lang="en">
<head>
<meta charset="utf-8">
<title>Hand Soap Sticker – BRENOSKI</title>
<link rel="stylesheet" href="https://fonts.googleapis.com/css2?family=Bebas+Neue&family=Montserrat:wght@800&display=swap">
<style>
  :root {
    --canvas: #ffffff;
    --border-light: #f2f3f3;
    --border-shade: #dfe2e2;
    --label-light: #94c43d;
    --label-dark: #6f9f35;
    --label-text: #ffffff;
    --ink: #111111;
  }
  * { margin: 0; padding: 0; box-sizing: border-box; }
  html, body {
    width: 885px;
    height: 1200px;
    overflow: hidden;
    background: var(--canvas);
  }
  .sticker {
    position: relative;
    width: 885px;
    height: 1200px;
  }
  .sticker-border {
    position: absolute;
    left: 23px;
    top: 15px;
    width: 837px;
    height: 790px;
    border-radius: 46% 46% 50% 50% / 30% 30% 70% 70%;
    background: linear-gradient(180deg, var(--border-light), var(--border-shade));
    box-shadow: 0 8px 10px rgba(110, 160, 50, 0.35);
  }
  .label-area {
    position: absolute;
    left: 62px;
    top: 50px;
    width: 761px;
    height: 700px;
    border-radius: 46% 46% 50% 50% / 30% 30% 70% 70%;
    background: linear-gradient(160deg, var(--label-light), var(--label-dark));
  }
  .product-name {
    position: absolute;
    left: 0;
    top: 298px;
    width: 885px;
    text-align: center;
    font-family: "Bebas Neue", "Impact", sans-serif;
    font-weight: 400;
    font-size: 180px;
    line-height: 1;
    letter-spacing: 6px;
    color: var(--label-text);
  }
  .powered-label {
    position: absolute;
    left: 258px;
    top: 940px;
    font-family: "Montserrat", "Arial", sans-serif;
    font-weight: 800;
    font-size: 18px;
    color: var(--ink);
  }
  .brand-name {
    position: absolute;
    left: 0;
    top: 1000px;
    width: 885px;
    text-align: center;
    font-family: "Montserrat", "Arial", sans-serif;
    font-weight: 800;
    font-size: 44px;
    line-height: 1;
    color: var(--ink);
  }
</style>
</head>
<body>
  <main class="sticker">
    <div class="sticker-border" aria-hidden="true"></div>
    <div class="label-area" role="img" aria-label="Green leaf-shaped sticker illustration"></div>

    <h1 class="product-name">HAND SOAP</h1>

    <p class="powered-label">powered by</p>
    <p class="brand-name">BRENOSKI</p>
  </main>
</body>
</html>
```